Tree Service Billboard 20x8 ft

We need a billboard design for a tree service company.
The billboard is 20ft x 8 ft so we need a design that is capable to stretching to those dimensions without loosing quality.
I have attached a series of images.
Image 1- Simply a billboard that I think looks good that I would like you to use for inspiration. I am aiming for the same format only no color in the wording, just black white, or gray. I like the the trees in the background, the logo placed to the left, and wording on the right.
Image 2- Current Logo I would like to the left of the billboard
Image 3- Another format of current logo if needed.
Image 4- A drawn out design template
Image 5- Another drawn out design template

Specific things I am looking for
-The contact number to be the largest thing on the design
-The logo on the design
-Key points to the design to say:
Tree Removal
Tree Trimming
Land Development
Stump Grinding
Storm Response
Insured
Free Bids
-The facebook logo
-The Google Logo

```html
<!DOCTYPE html>
<html lang="en">
<head>
<meta charset="utf-8">
<title>Birch Line Tree Service – Billboard</title>
<link rel="stylesheet" href="https://fonts.googleapis.com/css2?family=Bebas+Neue&family=Oswald:wght@300;600;700&display=swap">
<style>
  :root {
    --ink: #0d0d0d;
    --stone: #6c6c6c;
    --paper: #f8f8f8;
    --ground: #e4e6e8;
    --band-grey: #6b6b6b;
    --white: #ffffff;
    --star: #f4b400;
  }
  * { margin: 0; padding: 0; box-sizing: border-box; }
  html, body { width: 1200px; height: 840px; overflow: hidden; }
  body { background: var(--ground); position: relative; font-family: "Bebas Neue", sans-serif; }

  .billboard {
    position: absolute; left: 0; top: 180px;
    width: 1200px; height: 480px;
    background: var(--paper);
    overflow: hidden;
  }

  .service { position: absolute; font-size: 46px; line-height: 1; letter-spacing: 0.5px; white-space: nowrap; }
  .service--dark { color: var(--ink); }
  .service--grey { color: var(--stone); }
  .service-list--left .service { text-align: right; right: 0; }
  .service-list--left { position: absolute; left: 0; top: 0; width: 396px; height: 260px; }
  .service-list--right { position: absolute; left: 793px; top: 0; width: 400px; height: 260px; }
  .service-list--right .service { left: 0; }

  .leaders { position: absolute; left: 0; top: 0; }

  .brand-mark {
    position: absolute; left: 468px; top: 20px;
    width: 220px; height: 220px;
    border: 7px solid var(--ink); border-radius: 50%;
    display: flex; align-items: center; justify-content: center;
    font-size: 46px; color: var(--ink); text-align: center; line-height: 0.95;
  }

  .company-name {
    position: absolute; left: 0; width: 1200px; top: 248px;
    text-align: center; font-size: 84px; color: var(--stone);
    letter-spacing: 1px; padding-right: 40px;
  }

  .contact-band { position: absolute; left: 0; bottom: 0; width: 1200px; height: 124px; }

  .phone {
    position: absolute; left: 96px; top: 356px;
    font-family: "Oswald", sans-serif; font-weight: 700;
    font-size: 98px; line-height: 124px; color: var(--white);
    letter-spacing: -1px;
  }
  .phone-icon { position: absolute; left: 26px; top: 384px; width: 62px; height: 62px; }

  .social { position: absolute; left: 700px; top: 420px; display: flex; align-items: center; gap: 8px; }
  .social-dot { width: 30px; height: 30px; border-radius: 50%; background: var(--ink); }
  .social-handle { font-family: "Oswald", sans-serif; font-weight: 300; font-size: 30px; color: var(--ink); line-height: 1; }

  .review-badge {
    position: absolute; left: 1050px; top: 414px;
    width: 106px; height: 42px; border-radius: 8px;
    background: var(--white); opacity: 0.9;
  }
</style>
</head>
<body>
  <main class="billboard">
    <svg class="leaders" width="1200" height="260" viewBox="0 0 1200 260" aria-hidden="true">
      <g stroke="#0d0d0d" stroke-width="1.6" fill="#0d0d0d">
        <line x1="404" y1="78" x2="490" y2="76"/><circle cx="404" cy="78" r="2.6"/>
        <line x1="392" y1="146" x2="476" y2="144"/><circle cx="392" cy="146" r="2.6"/>
        <line x1="404" y1="212" x2="490" y2="211"/><circle cx="404" cy="212" r="2.6"/>
        <line x1="697" y1="70" x2="783" y2="68"/><circle cx="783" cy="68" r="2.6"/>
        <line x1="710" y1="137" x2="796" y2="136"/><circle cx="796" cy="136" r="2.6"/>
        <line x1="697" y1="205" x2="783" y2="204"/><circle cx="783" cy="204" r="2.6"/>
      </g>
    </svg>

    <div class="service-list service-list--left">
      <p class="service service--dark" style="top:56px">Tree Removal</p>
      <p class="service service--grey" style="top:124px; right:14px">Tree Trimming</p>
      <p class="service service--dark" style="top:190px">Storm Response</p>
    </div>

    <div class="brand-mark">Birch<br>Line</div>

    <div class="service-list service-list--right">
      <p class="service service--dark" style="top:46px">Land Development</p>
      <p class="service service--grey" style="top:114px; left:12px">Stump Grinding</p>
      <p class="service service--dark" style="top:182px">Insured &amp; Free Bids</p>
    </div>

    <h1 class="company-name">Birch Line Tree Service</h1>

    <svg class="contact-band" viewBox="0 0 1200 124" preserveAspectRatio="none" aria-hidden="true">
      <polygon points="0,24 1200,24 1200,124 0,124" fill="#6b6b6b" transform="translate(0,2)"/>
      <path d="M0,0 H596 Q612,0 622,12 L690,124 H0 Z" fill="#0d0d0d"/>
    </svg>

    <svg class="phone-icon" viewBox="0 0 62 62" aria-hidden="true">
      <circle cx="31" cy="31" r="28" fill="none" stroke="#fff" stroke-width="3"/>
      <path d="M20 15c2-1 4-1 5 1l3 6c1 2 0 3-1 4l-2 2c2 4 5 7 9 9l2-2c1-1 2-2 4-1l6 3c2 1 2 3 1 5l-2 3c-2 2-5 2-8 1-9-4-16-11-20-20-1-3-1-6 1-8z" fill="#fff"/>
    </svg>
    <p class="phone">417-555-0148</p>

    <div class="social">
      <span class="social-dot" aria-hidden="true"></span>
      <span class="social-handle">MarlowBirchTreeService</span>
    </div>

    <div class="review-badge" role="img" aria-label="Review listing badge"></div>
  </main>
</body>
</html>
```